International wholesale business needs a business card

We need a business card.

Company Details:
Company Name and logo
Address, Phone number, Website
Employee Details:
Name, Designation, Mobile Number & Email address

Logo file is attached.

```html
<!DOCTYPE html>
<html lang="en">
<head>
<meta charset="utf-8">
<title>Velora Trading – Business Card</title>
<link rel="stylesheet" href="https://fonts.googleapis.com/css2?family=Poppins:wght@400;500;600&display=swap">
<style>
  :root {
    --backdrop: #ececec;
    --card-light: #f4f4f3;
    --card-dark: #060606;
    --brand-red: #c7262e;
    --brand-grey: #9a9a9a;
    --ink: #141414;
  }
  * { box-sizing: border-box; margin: 0; padding: 0; }
  html, body {
    width: 1200px; height: 721px; overflow: hidden;
    background: var(--backdrop);
    font-family: "Poppins", sans-serif;
  }
  .canvas {
    position: relative; width: 1200px; height: 721px;
    display: flex; align-items: center; justify-content: center; gap: 60px;
  }
  .card {
    position: relative; width: 500px; height: 286px;
    box-shadow: 0 14px 30px rgba(0,0,0,0.18);
  }
  .card--front { background: var(--card-light); color: var(--ink); }
  .card--back { background: var(--card-dark); }

  .brand {
    display: flex; align-items: center; gap: 12px;
    color: var(--brand-red); font-weight: 600; letter-spacing: 0.06em;
    text-transform: uppercase; white-space: nowrap;
  }
  .brand__dot {
    flex: none; border-radius: 50%; background: var(--brand-red);
  }

  .card--front .brand { position: absolute; right: 40px; top: 62px; font-size: 22px; }
  .card--front .brand__dot { width: 26px; height: 26px; }

  .holder { position: absolute; left: 38px; top: 40px; }
  .holder__name { font-size: 15px; font-weight: 600; letter-spacing: 0.04em; text-transform: uppercase; }
  .holder__role { font-size: 11px; letter-spacing: 0.08em; text-transform: uppercase; margin-top: 1px; }

  .divider {
    position: absolute; left: 38px; top: 112px; width: 370px; height: 1.5px;
    background: var(--brand-red);
  }

  .contact { position: absolute; left: 38px; top: 128px; list-style: none; }
  .contact li { font-size: 9.5px; letter-spacing: 0.1em; text-transform: uppercase; line-height: 1.6; }

  .address { position: absolute; right: 40px; bottom: 34px; font-style: normal; text-align: left; }
  .address span { display: block; font-size: 9.5px; letter-spacing: 0.1em; text-transform: uppercase; line-height: 1.6; }

  .card--back .brand { position: absolute; left: 50%; top: 96px; transform: translateX(-50%); font-size: 32px; }
  .card--back .brand__dot { width: 40px; height: 40px; }
  .card--back .site {
    position: absolute; left: 0; right: 0; top: 200px; text-align: center;
    color: var(--brand-grey); font-size: 10px; letter-spacing: 0.22em; text-transform: uppercase;
  }
</style>
</head>
<body>
<main class="canvas">
  <section class="card card--front" aria-label="Business card front">
    <div class="holder">
      <p class="holder__name">Marcus Hale</p>
      <p class="holder__role">Manager</p>
    </div>
    <div class="brand"><span class="brand__dot"></span>Velora Trading</div>
    <div class="divider"></div>
    <ul class="contact">
      <li>555 210 4830</li>
      <li>hello@veloratrading.com</li>
      <li>www.veloratrading.com</li>
    </ul>
    <address class="address">
      <span>48 Harbor Street,</span>
      <span>Millbrook, TN 37201</span>
    </address>
  </section>

  <section class="card card--back" aria-label="Business card back">
    <div class="brand"><span class="brand__dot"></span>Velora Trading</div>
    <p class="site">www.veloratrading.com</p>
  </section>
</main>
</body>
</html>
```